Change consultancy needs business card+ design

We need business card design for a Seattle based consulting firm called
Harlow + Dunmore. Our firm helps organizations shift their paradigms, lean into change, and reimagine the way they work together.
**Updated**
Our firm name is the logo using black and orange font, see attached. We would like to include the tagline "(Re)shaping how teams connect"
The final design should find a balance between playful, edgy and professional. For example, we are using the attached goldfish photo on our homepage and like the colors and concept of leaping forward. However, don't want to use the image on the card.
Lastly, depending on the winning design, we will also be looking for stationary/template design that will compliment the business card.
- Helvetica

```html
<!DOCTYPE html>
<html lang="en">
<head>
<meta charset="utf-8">
<title>Harlow + Dunmore — Business Card</title>
<link rel="stylesheet" href="https://fonts.googleapis.com/css2?family=Arimo:wght@400&family=Open+Sans:wght@600;700&display=swap">
<style>
  :root {
    --orange: #f7921e;
    --white: #ffffff;
    --black: #000000;
    --ink: #111111;
    --backdrop: #e9e6e1;
    --rule: #8a8a8a;
  }
  * { box-sizing: border-box; margin: 0; padding: 0; }
  html, body {
    width: 1200px;
    height: 844px;
    overflow: hidden;
    background: var(--backdrop);
  }
  .stage {
    position: relative;
    width: 1200px;
    height: 844px;
    display: flex;
    align-items: center;
    justify-content: center;
    gap: 40px;
  }
  .card {
    position: relative;
    width: 540px;
    height: 340px;
    border-radius: 22px;
    overflow: hidden;
    box-shadow: 0 6px 18px rgba(0,0,0,0.18);
  }

  /* Front */
  .card--front {
    display: flex;
    flex-direction: column;
    background: var(--black);
  }
  .front__band-top {
    height: 128px;
    background: var(--orange);
  }
  .front__band-brand {
    height: 104px;
    background: var(--white);
    display: flex;
    flex-direction: column;
    align-items: center;
    justify-content: center;
    padding-top: 4px;
  }
  .brand-name {
    font-family: "Arimo", "Helvetica Neue", Helvetica, Arial, sans-serif;
    font-weight: 400;
    font-size: 46px;
    letter-spacing: -0.5px;
    line-height: 1;
    color: var(--ink);
    white-space: nowrap;
  }
  .brand-tagline {
    margin-top: 6px;
    font-family: "Open Sans", Helvetica, Arial, sans-serif;
    font-weight: 600;
    font-size: 15px;
    letter-spacing: 0.3px;
    color: var(--orange);
    text-transform: uppercase;
    white-space: nowrap;
  }
  .front__band-base {
    flex: 1;
    background: var(--black);
  }

  /* Back */
  .card--back {
    background: var(--black);
    font-family: "Open Sans", Helvetica, Arial, sans-serif;
  }
  .contact-person {
    position: absolute;
    right: 44px;
    top: 112px;
    text-align: right;
  }
  .person-name {
    font-weight: 700;
    font-size: 25px;
    letter-spacing: 0.5px;
    color: var(--orange);
    text-transform: uppercase;
    white-space: nowrap;
  }
  .person-role {
    margin-top: 6px;
    font-weight: 600;
    font-size: 15px;
    letter-spacing: 0.3px;
    color: var(--white);
    text-transform: uppercase;
    white-space: nowrap;
  }
  .contact-lines {
    position: absolute;
    right: 44px;
    top: 205px;
    display: flex;
    align-items: center;
    gap: 34px;
    font-weight: 600;
    font-size: 15px;
    color: var(--white);
    white-space: nowrap;
  }
  .contact-divider {
    width: 1px;
    height: 30px;
    background: var(--rule);
  }
</style>
</head>
<body>
  <main class="stage">
    <section class="card card--front" aria-label="Business card front">
      <div class="front__band-top"></div>
      <div class="front__band-brand">
        <h1 class="brand-name">Harlow + Dunmore</h1>
        <p class="brand-tagline">(Re)shaping how teams connect</p>
      </div>
      <div class="front__band-base"></div>
    </section>

    <section class="card card--back" aria-label="Business card back">
      <div class="contact-person">
        <h2 class="person-name">Nora Harlow</h2>
        <p class="person-role">Managing Partner</p>
      </div>
      <div class="contact-lines">
        <span class="contact-phone">206.555.0147</span>
        <span class="contact-divider" aria-hidden="true"></span>
        <span class="contact-web">www.harlowdunmore.com</span>
      </div>
    </section>
  </main>
</body>
</html>
```